Dating Coach needs a Book Cover Design

My new book called "When to Turn the Tide: Meeting Romance Among the Endless Crowd of Digital Courtship" needs a cover! I tried to make one on my own, but it's just not my skill set :) Please see attached for my best attempt. I'd like to see the title smaller and the tagline bigger - so that the tagline is easier to read. But I'm not sure how to do this and still have the Title look great. I'm also considering if the "TURN THE TIDE" part should not be in all caps. Looking forward to your ideas! I'm also afraid that the drawing is a bit too cartoonish and doesn't match my brand. I'm looking for something elegant and also very approachable and down to earth. My website is www.petrawendtcoaching.example so you can use as reference! Please see my attached brand style guide for colors. This will be an e-book that I give away for free to anyone who signs up for my newsletter. Some mock-ups would also be great to use in advertising.

```html
<!DOCTYPE html>
<html lang="en">
<head>
<meta charset="utf-8">
<title>When to Turn the Tide – Book Cover</title>
<link rel="stylesheet" href="https://fonts.googleapis.com/css2?family=Pinyon+Script&family=Marcellus&display=swap">
<style>
  :root {
    --plum: #7a5683;
    --cream: #ecdcc6;
    --gold: #e9b36a;
    --gold-deep: #c98a3e;
    --gold-pale: #f6d39b;
    --brass: #a08a4a;
  }
  html, body {
    margin: 0;
    padding: 0;
    width: 750px;
    height: 1200px;
    overflow: hidden;
    background: var(--plum);
  }
  .cover {
    position: relative;
    width: 750px;
    height: 1200px;
    background: var(--plum);
    color: var(--cream);
    overflow: hidden;
  }
  .title-script {
    position: absolute;
    top: 52px;
    left: 0;
    width: 750px;
    text-align: center;
    font-family: "Pinyon Script", cursive;
    font-size: 74px;
    line-height: 1;
    white-space: nowrap;
  }
  .title-main {
    position: absolute;
    top: 160px;
    left: 0;
    width: 750px;
    text-align: center;
    font-family: "Marcellus", serif;
    font-size: 106px;
    line-height: 1;
    letter-spacing: 2px;
  }
  .title-rule {
    position: absolute;
    top: 267px;
    left: 92px;
    width: 574px;
    height: 2px;
    background: var(--cream);
  }
  .subtitle {
    position: absolute;
    top: 298px;
    left: 0;
    width: 750px;
    text-align: center;
    font-family: "Marcellus", serif;
    font-size: 33px;
    line-height: 44px;
    letter-spacing: 1px;
  }
  .subtitle .emphasis {
    text-transform: uppercase;
    letter-spacing: 2px;
  }
  .cover-art {
    position: absolute;
    top: 410px;
    left: 0;
    width: 750px;
    height: 626px;
    background:
      radial-gradient(ellipse 60% 75% at 50% 95%, var(--gold-pale) 0%, var(--gold) 45%, var(--gold-deep) 70%, rgba(201,138,62,0) 100%);
  }
  .band-rule {
    position: absolute;
    top: 1035px;
    left: 0;
    width: 750px;
    height: 2px;
    background: var(--cream);
    opacity: 0.8;
  }
  .imprint {
    position: absolute;
    top: 1100px;
    left: 0;
    width: 750px;
    display: flex;
    align-items: center;
    justify-content: center;
    gap: 22px;
  }
  .imprint-mark {
    width: 40px;
    height: 40px;
    border: 2px solid var(--brass);
    border-radius: 50%;
    box-sizing: border-box;
  }
  .imprint-name {
    font-family: "Marcellus", serif;
    font-size: 32px;
    letter-spacing: 1px;
    color: var(--cream);
  }
</style>
</head>
<body>
  <main class="cover">
    <h1 class="title">
      <span class="title-script">When To Turn The</span>
      <span class="title-main">TIDE</span>
    </h1>
    <div class="title-rule"></div>
    <p class="subtitle">
      Meeting Romance<br>
      Among the Endless Crowd of<br>
      <span class="emphasis">Digital Courtship</span>
    </p>
    <div class="cover-art" role="img" aria-label="Photograph of a golden haystack with a gold heart-topped pin stuck into it"></div>
    <div class="band-rule"></div>
    <div class="imprint">
      <span class="imprint-mark"></span>
      <span class="imprint-name">Petra Wendt Coaching</span>
    </div>
  </main>
</body>
</html>
```